Postcard

We are looking to have a two sided, 6"x9", postcard created for our landscaping and snowplowing company.
I have attached the latest design for our business cards as well as our logo. We would like the design to incorporate similar design with images of beautiful residential lawns and gardens.
Target Market(s)
Residential homeowners in West Michigan
Industry/Entity Type
Landscaping
Font styles to use
Serif
Sans Serif
Colors
Designer to choose colors to be used in the design.
Requirements
Must have
- Should look conservative but lots of color. Images of gorgeous lawns and landscape gardens at nice homes
Nice to have
- Easy to read, looks nice.. Should fit in with the images I have uploaded.
Should not have
- Should not be ostentatious.

```html
<!DOCTYPE html>
<html lang="en">
<head>
<meta charset="utf-8">
<title>Maple Run Landscaping – Postcard</title>
<link rel="stylesheet" href="https://fonts.googleapis.com/css2?family=Raleway:wght@400;600;700&family=Cormorant+Garamond:wght@500&display=swap">
<style>
  :root {
    --backdrop: #1d1d1d;
    --paper: #ffffff;
    --ink-black: #000000;
    --cream: #eef3da;
    --brand-blue: #0a8fd6;
    --deep-blue: #1565a8;
    --lime: #c9dc1c;
    --leaf: #1f8f3a;
    --forest: #0f5a25;
    --logo-grey: #8a8d8f;
    --text-dark: #2a2a2a;
    --contact-blue: #1a6fb0;
  }
  * { margin: 0; padding: 0; box-sizing: border-box; }
  html, body { width: 1200px; height: 1200px; overflow: hidden; background: var(--backdrop); }
  .postcard {
    position: absolute;
    top: 214px;
    width: 518px;
    height: 777px;
    background: var(--paper);
  }
  .postcard--front { left: 69px; }
  .postcard--back { left: 603px; }
  .postcard__art {
    position: absolute;
    left: 29px;
    top: 29px;
    width: 460px;
    height: 720px;
    display: block;
  }
  .brand-name { font-family: "Cormorant Garamond", serif; font-weight: 500; }
  .brand-sub { font-family: "Raleway", sans-serif; font-weight: 400; }
  .service-list { font-family: "Raleway", sans-serif; font-size: 15px; fill: #ffffff; opacity: .88; }
  .front-phone { font-family: "Raleway", sans-serif; font-weight: 700; font-size: 27px; letter-spacing: 9px; fill: #ffffff; }
  .contact { font-family: "Raleway", sans-serif; font-size: 15px; fill: var(--contact-blue); }
  .contact--phone { font-weight: 700; }
  .address { font-family: "Raleway", sans-serif; font-size: 11.5px; fill: var(--text-dark); }
</style>
</head>
<body>

<section class="postcard postcard--front">
  <svg class="postcard__art" viewBox="0 0 575 900" xmlns="http://www.w3.org/2000/svg">
    <defs>
      <linearGradient id="frontPhotoTone" x1="0" y1="0" x2="0" y2="1">
        <stop offset="0" stop-color="#b9cfe3"/>
        <stop offset=".35" stop-color="#6f7a4a"/>
        <stop offset=".7" stop-color="#5f8a2c"/>
        <stop offset="1" stop-color="#8fb43a"/>
      </linearGradient>
      <linearGradient id="gardenTone" x1="0" y1="0" x2="0" y2="1">
        <stop offset="0" stop-color="#1a8c34"/>
        <stop offset=".6" stop-color="#3c8a2a"/>
        <stop offset="1" stop-color="#1d6a22"/>
      </linearGradient>
      <linearGradient id="blueSweep" x1="0" y1="0" x2="1" y2="0">
        <stop offset="0" stop-color="var(--deep-blue)"/>
        <stop offset=".6" stop-color="var(--brand-blue)"/>
        <stop offset="1" stop-color="#3fc0f0"/>
      </linearGradient>
      <linearGradient id="limeSweep" x1="0" y1="0" x2="1" y2="0">
        <stop offset="0" stop-color="var(--leaf)"/>
        <stop offset="1" stop-color="var(--lime)"/>
      </linearGradient>
    </defs>

    <rect class="front-base" width="575" height="900" fill="var(--ink-black)"/>

    <path role="img" aria-label="Photo of a manor house with a formal topiary garden and stone fountain"
          d="M0,0 H575 V282 Q330,400 0,378 Z" fill="url(#frontPhotoTone)"/>

    <path class="accent-lime" d="M170,412 Q430,395 575,318 V336 Q430,410 250,420 Z" fill="url(#limeSweep)"/>
    <path class="accent-blue" d="M0,378 Q330,400 575,282 V318 Q350,440 0,392 Z" fill="url(#blueSweep)"/>

    <g class="brand brand--front" text-anchor="middle">
      <text class="brand-name" x="287" y="514" font-size="48" letter-spacing="12" fill="var(--logo-grey)">MAPLE RUN</text>
      <line x1="110" y1="526" x2="455" y2="526" stroke="var(--leaf)" stroke-width="2"/>
      <text class="brand-sub" x="290" y="547" font-size="13" letter-spacing="14" fill="var(--leaf)">LANDSCAPING</text>
    </g>

    <path role="img" aria-label="Soft photo of a sculpted hedge garden behind the service list"
          d="M0,612 Q260,540 575,736 V900 H0 Z" fill="url(#gardenTone)"/>
    <path class="accent-garden-edge" d="M0,612 Q260,540 575,736" fill="none" stroke="url(#limeSweep)" stroke-width="5"/>

    <g class="service-list">
      <g fill="#ffffff">
        <circle cx="86" cy="638" r="3"/><circle cx="86" cy="664" r="3"/><circle cx="86" cy="690" r="3"/>
        <circle cx="86" cy="716" r="3"/><circle cx="86" cy="742" r="3"/><circle cx="86" cy="768" r="3"/>
        <circle cx="86" cy="795" r="3"/><circle cx="86" cy="821" r="3"/>
      </g>
      <text x="112" y="643">Landscape design &amp; installation</text>
      <text x="112" y="669">Professional lawn maintenance</text>
      <text x="112" y="695">Spring &amp; fall leaf cleanup</text>
      <text x="112" y="721">Irrigation system installation &amp; maintenance</text>
      <text x="112" y="747">Snowplowing</text>
      <text x="112" y="773">Fertilizer &amp; weed control</text>
      <text x="112" y="800">Tree maintenance &amp; removal</text>
      <text x="112" y="826">Landscape bed maintenance</text>
    </g>

    <g class="phone-line">
      <path d="M132,862 q-4,0 -5,5 q0,14 16,18 q5,-1 5,-5 l-5,-4 q-2,2 -4,2 q-6,-3 -7,-8 q0,-2 2,-3 z" fill="#ffffff"/>
      <text class="front-phone" x="166" y="882">616.555.0142</text>
    </g>
  </svg>
</section>

<section class="postcard postcard--back">
  <svg class="postcard__art" viewBox="0 0 575 900" xmlns="http://www.w3.org/2000/svg">
    <defs>
      <linearGradient id="frameSides" x1="0" y1="0" x2="1" y2="0">
        <stop offset="0" stop-color="var(--leaf)"/>
        <stop offset=".35" stop-color="#c89a12"/>
        <stop offset=".6" stop-color="var(--lime)"/>
        <stop offset="1" stop-color="#e2d200"/>
      </linearGradient>
      <linearGradient id="frameFade" x1="0" y1="0" x2="0" y2="1">
        <stop offset=".35" stop-color="var(--cream)" stop-opacity="1"/>
        <stop offset=".7" stop-color="var(--cream)" stop-opacity="0"/>
      </linearGradient>
      <linearGradient id="backPhotoTone" x1="0" y1="0" x2="0" y2="1">
        <stop offset="0" stop-color="#7fb2dd"/>
        <stop offset=".35" stop-color="#2e6a3a"/>
        <stop offset=".7" stop-color="#4d9a2c"/>
        <stop offset="1" stop-color="#3e8a24"/>
      </linearGradient>
      <linearGradient id="goldSweep" x1="0" y1="0" x2="1" y2="0">
        <stop offset="0" stop-color="var(--leaf)"/>
        <stop offset=".2" stop-color="#c89a12"/>
        <stop offset=".5" stop-color="var(--lime)"/>
        <stop offset="1" stop-color="var(--brand-blue)"/>
      </linearGradient>
      <linearGradient id="backBlue" x1="0" y1="0" x2="1" y2="0">
        <stop offset="0" stop-color="var(--brand-blue)"/>
        <stop offset="1" stop-color="var(--deep-blue)"/>
      </linearGradient>
    </defs>

    <rect class="frame" width="575" height="900" fill="url(#frameSides)"/>
    <rect class="frame-fade" width="575" height="900" fill="url(#frameFade)"/>
    <rect class="address-panel" x="15" y="0" width="546" height="885" fill="var(--cream)"/>

    <path class="band-blue" d="M0,290 Q330,330 575,215 V318 Q330,470 0,412 Z" fill="url(#backBlue)"/>
    <path class="band-black" d="M0,305 Q330,345 575,228 V298 Q330,430 0,360 Z" fill="var(--ink-black)"/>
    <path class="band-gold" d="M0,278 Q330,330 575,212 V240 Q330,360 0,322 Z" fill="url(#goldSweep)"/>
    <path role="img" aria-label="Photo of a lit family home at dusk with a wide green lawn, pines and flower beds"
          d="M0,0 H575 V215 Q330,330 0,280 Z" fill="url(#backPhotoTone)"/>

    <g class="brand brand--back" text-anchor="middle">
      <text class="brand-name" x="417" y="458" font-size="26" letter-spacing="6" fill="var(--text-dark)">MAPLE RUN</text>
      <line x1="340" y1="465" x2="494" y2="465" stroke="var(--leaf)" stroke-width="1"/>
      <text class="brand-sub" x="418" y="476" font-size="7" letter-spacing="6" fill="var(--leaf)">LANDSCAPING</text>
    </g>

    <g class="contact-list">
      <path d="M311,495 q-3,0 -3,4 q0,10 11,12 q3,0 3,-3 l-3,-3 q-1,1 -3,1 q-4,-2 -5,-6 q0,-1 1,-2 z" fill="var(--leaf)"/>
      <text class="contact contact--phone" x="333" y="508">616.555.0142</text>
      <rect x="308" y="522" width="14" height="9" fill="var(--leaf)"/>
      <path d="M308,522 l7,5 l7,-5" fill="none" stroke="var(--cream)" stroke-width="1"/>
      <text class="contact" x="333" y="531">hello@maplerunlawn.com</text>
      <g fill="none" stroke="var(--leaf)" stroke-width="1.3">
        <circle cx="315" cy="549" r="6"/>
        <ellipse cx="315" cy="549" rx="2.5" ry="6"/>
        <line x1="309" y1="549" x2="321" y2="549"/>
      </g>
      <text class="contact" x="333" y="554">www.maplerunlawn.com</text>
    </g>

    <path class="pin" d="M86,617 a11,11 0 0 1 11,11 c0,8 -11,19 -11,19 c0,0 -11,-11 -11,-19 a11,11 0 0 1 11,-11 z M86,623 a5,5 0 1 0 0.01,0 z"
          fill="var(--contact-blue)" fill-rule="evenodd"/>
    <text class="address" x="63" y="665">1840 Birchwood Lane SE,</text>
    <text class="address" x="63" y="682">Grand Rapids, Michigan 49546</text>

    <rect class="stamp-box" x="308" y="597" width="204" height="105" fill="none" stroke="#8c8c8c" stroke-width="1" stroke-dasharray="2 2"/>

    <g class="mailing-lines" stroke="#9a9a9a" stroke-width="1" stroke-dasharray="1.5 2">
      <line x1="63" y1="743" x2="512" y2="743"/>
      <line x1="63" y1="772" x2="512" y2="772"/>
      <line x1="63" y1="801" x2="512" y2="801"/>
      <line x1="63" y1="831" x2="512" y2="831"/>
      <line x1="63" y1="860" x2="512" y2="860"/>
    </g>
  </svg>
</section>

</body>
</html>
```